Real estate investor business card to retire young ;)!

I need a logo design and a business card. I am based in Montreal, Canada. I buy multi-family properties and do lots development. The final design should communicate that I am a problem solver and reliable.

This card will be given to other investors, to potential sellers and industry experts.

Target Market(s)

Real estate community, multi-family owners

Industry/Entity Type

Real Estate Development

Contact Information for Business Card

My name: Lorna Vickery
email: immo.lorna.vickery@quellmail.example
cellphone: (555) 274-3916

Logo Text

Gestion immobilière

Font styles to use
Sans Serif

Colors
3176b5

Requirements
Must have
• Within 1-2 seconds the person who sees my card should know that I buy properties and lot. Areas to for Phone number and email adress. I do not have a business name. The card should simply state my name and what I do. The logo should be remembered by the person who reads my card
Should not have
• Colors too bright. Too much small details. I want something balanced, bold without being agressive.

```html
<!DOCTYPE html>
<html lang="en">
<head>
<meta charset="UTF-8">
<title>Lorna Vickery – Business Card</title>
<link rel="stylesheet" href="https://fonts.googleapis.com/css2?family=Open+Sans:wght@400;700;800&display=swap">
<style>
  :root {
    --page-bg: #1d2024;
    --card-bg: #221f20;
    --brand-blue: #3176b5;
    --text-white: #f2f2f2;
    --text-grey: #b8b8b8;
  }
  * { margin: 0; padding: 0; box-sizing: border-box; }
  html, body {
    width: 1200px;
    height: 900px;
    overflow: hidden;
    background: var(--page-bg);
    font-family: "Open Sans", Arial, sans-serif;
  }
  .sheet {
    width: 1200px;
    height: 900px;
    display: flex;
    flex-direction: column;
    align-items: center;
    justify-content: center;
    gap: 60px;
  }
  .card {
    width: 620px;
    height: 354px;
    background: var(--card-bg);
    border-radius: 26px;
    box-shadow: 0 10px 30px rgba(0, 0, 0, 0.45);
    display: flex;
    align-items: center;
    justify-content: center;
  }

  /* name mark */
  .wordmark {
    display: flex;
    align-items: center;
    gap: 14px;
    color: var(--brand-blue);
    white-space: nowrap;
  }
  .wordmark__square {
    width: 40px;
    height: 40px;
    background: var(--brand-blue);
    flex: none;
  }
  .wordmark__text { display: flex; flex-direction: column; }
  .wordmark__name {
    font-size: 38px;
    font-weight: 800;
    letter-spacing: 2px;
    line-height: 1.05;
  }
  .wordmark__tagline {
    font-size: 12px;
    font-weight: 400;
    letter-spacing: 4px;
    text-transform: uppercase;
    margin-top: 4px;
  }

  /* front side */
  .card--front { padding: 0 28px; }
  .contact {
    text-align: right;
    padding-right: 20px;
    white-space: nowrap;
  }
  .contact__name {
    color: var(--text-white);
    font-weight: 700;
    font-size: 18px;
    letter-spacing: 2px;
    margin-bottom: 8px;
  }
  .contact__line {
    color: var(--text-grey);
    font-size: 11.5px;
    letter-spacing: 0.8px;
    display: flex;
    justify-content: flex-end;
    align-items: center;
    gap: 7px;
    margin-top: 7px;
  }
  .contact__phone { font-size: 14px; letter-spacing: 3px; }
  .contact__icon { width: 11px; height: 11px; flex: none; }
  .divider {
    width: 2px;
    height: 110px;
    background: var(--brand-blue);
    margin-right: 20px;
    flex: none;
  }
  .card--front .wordmark { gap: 10px; }
  .card--front .wordmark__square { width: 26px; height: 26px; }
  .card--front .wordmark__name { font-size: 25px; letter-spacing: 1px; }
  .card--front .wordmark__tagline { font-size: 8.5px; letter-spacing: 2.6px; margin-top: 2px; }
</style>
</head>
<body>
  <main class="sheet">
    <section class="card card--front" aria-label="Card front with contact details">
      <div class="contact">
        <p class="contact__name">Lorna Vickery</p>
        <p class="contact__line contact__phone">(555) 274-3916
          <svg class="contact__icon" viewBox="0 0 12 12" aria-hidden="true">
            <rect x="3" y="0.5" width="6" height="11" rx="1" fill="var(--brand-blue)"/>
            <rect x="4" y="1.8" width="4" height="7" fill="var(--card-bg)"/>
          </svg>
        </p>
        <p class="contact__line">immo.lorna.vickery@quellmail.example
          <svg class="contact__icon" viewBox="0 0 12 12" aria-hidden="true">
            <rect x="0.5" y="2" width="11" height="8" fill="var(--brand-blue)"/>
            <path d="M0.5 2 L6 6.5 L11.5 2" stroke="var(--card-bg)" stroke-width="1.2" fill="none"/>
          </svg>
        </p>
      </div>
      <div class="divider"></div>
      <div class="wordmark">
        <span class="wordmark__square"></span>
        <span class="wordmark__text">
          <span class="wordmark__name">Lorna Vickery</span>
          <span class="wordmark__tagline">Gestion immobilière</span>
        </span>
      </div>
    </section>

    <section class="card card--back" aria-label="Card back with name mark">
      <div class="wordmark">
        <span class="wordmark__square"></span>
        <span class="wordmark__text">
          <span class="wordmark__name">Lorna Vickery</span>
          <span class="wordmark__tagline">Gestion immobilière</span>
        </span>
      </div>
    </section>
  </main>
</body>
</html>
```